CareVantRx business cards

We need a business card design that we could customize as needed for employees. We will need space for Name, Title, 1-2 phone numbers and email address.

We are a Pharmacy Benefits Management (PBM) company for hospice agencies and beginning a nationwide expansion. Attached is a vector file of our logo.

Cards can be single or double sided.

Industry/Entity Type

Business

```html
<!DOCTYPE html>
<html lang="en">
<head>
<meta charset="utf-8">
<title>CareVantRx Business Cards</title>
<link rel="stylesheet" href="https://fonts.googleapis.com/css2?family=Source+Sans+3:wght@400;600&display=swap">
<style>
  :root {
    --page-bg: #e9e7e3;
    --card-black: #000000;
    --brand-green: #8aa65a;
    --brand-green-muted: #88a05e;
    --brand-blue: #386b93;
    --text-light: #ffffff;
    --text-dark: #1e1e1e;
    --title-green: #8fae5c;
  }
  html, body {
    margin: 0;
    padding: 0;
    width: 1200px;
    height: 1186px;
    overflow: hidden;
    background: var(--page-bg);
    font-family: "Source Sans 3", "Myriad Pro", Arial, sans-serif;
  }
  .canvas {
    position: relative;
    width: 1200px;
    height: 1186px;
  }
  .card {
    position: absolute;
    overflow: hidden;
    box-shadow: 0 6px 18px rgba(0,0,0,0.18);
  }
  /* Front */
  .card-front {
    left: 279px;
    top: 52px;
    width: 880px;
    height: 504px;
    background: var(--card-black);
  }
  .card-front .swoosh {
    position: absolute;
    inset: 0;
    width: 100%;
    height: 100%;
  }
  .brand {
    position: absolute;
    left: 38px;
    top: 124px;
    display: flex;
    align-items: center;
    gap: 20px;
  }
  .brand-square {
    width: 92px;
    height: 92px;
    background: var(--brand-blue);
    border-radius: 8px;
  }
  .brand-name {
    font-size: 76px;
    font-weight: 400;
    color: var(--brand-green);
    line-height: 1;
    letter-spacing: -1px;
  }
  .person {
    position: absolute;
    left: 38px;
    top: 330px;
    color: var(--text-light);
  }
  .person-name {
    font-size: 31px;
    font-weight: 600;
    line-height: 1.2;
  }
  .person-title {
    font-size: 25px;
    color: var(--title-green);
    line-height: 1.3;
    margin-bottom: 10px;
  }
  .person-address {
    font-size: 19px;
    line-height: 1.72;
  }
  .contacts {
    position: absolute;
    right: 18px;
    top: 344px;
    margin: 0;
    padding: 0;
    list-style: none;
    color: var(--text-light);
    font-size: 21px;
    text-align: right;
  }
  .contacts li {
    display: flex;
    justify-content: flex-end;
    align-items: center;
    gap: 7px;
    height: 34px;
  }
  .contacts svg {
    width: 17px;
    height: 17px;
    fill: none;
    stroke: var(--text-light);
    stroke-width: 2;
  }
  /* Back */
  .card-back {
    left: 48px;
    top: 621px;
    width: 883px;
    height: 504px;
    background: var(--brand-green-muted);
  }
  .back-brand {
    position: absolute;
    left: 0;
    right: 60px;
    top: 180px;
    display: flex;
    justify-content: center;
    align-items: center;
    gap: 22px;
  }
  .back-brand .brand-square {
    width: 96px;
    height: 96px;
    background: #ffffff;
  }
  .back-brand .brand-name {
    color: #ffffff;
    font-size: 72px;
  }
  .back-web {
    position: absolute;
    left: 0;
    right: 60px;
    top: 412px;
    text-align: center;
    font-size: 34px;
    letter-spacing: 2px;
    color: var(--text-dark);
  }
</style>
</head>
<body>
<main class="canvas">

  <section class="card card-front" aria-label="Business card front">
    <svg class="swoosh" viewBox="0 0 510 292" preserveAspectRatio="none" aria-hidden="true">
      <path d="M440 0 C 432 150 300 262 150 292 L510 292 L510 0 Z" fill="var(--brand-green)"/>
      <path d="M510 30 C 462 172 334 262 160 292 L510 292 Z" fill="var(--brand-blue)"/>
    </svg>

    <div class="brand">
      <div class="brand-square"></div>
      <div class="brand-name">CareVantRx</div>
    </div>

    <div class="person">
      <div class="person-name">Your Name</div>
      <div class="person-title">Title</div>
      <div class="person-address">Sreet Name, City Name<br>Zip Code-00000</div>
    </div>

    <ul class="contacts">
      <li>
        <svg viewBox="0 0 16 16"><circle cx="8" cy="8" r="6.5"/><path d="M6 4.5 L5 6 C5.5 8.5 7.5 10.5 10 11 L11.5 10" /></svg>
        012-345-6789
      </li>
      <li>
        <svg viewBox="0 0 16 16"><rect x="2" y="7" width="12" height="6" rx="1"/><path d="M4 7 L5 3 H11 L12 7"/></svg>
        012-345-6789
      </li>
      <li>
        <svg viewBox="0 0 16 16"><rect x="1.5" y="3.5" width="13" height="9"/><path d="M1.5 3.5 L8 9 L14.5 3.5"/></svg>
        info@carevantrx.com
      </li>
      <li>
        <svg viewBox="0 0 16 16"><circle cx="8" cy="8" r="6.5"/><path d="M1.5 8 H14.5 M8 1.5 C5 5 5 11 8 14.5 M8 1.5 C11 5 11 11 8 14.5"/></svg>
        www.carevantrx.com
      </li>
    </ul>
  </section>

  <section class="card card-back" aria-label="Business card back">
    <div class="back-brand">
      <div class="brand-square"></div>
      <div class="brand-name">CareVantRx</div>
    </div>
    <div class="back-web">www.carevantrx.com</div>
  </section>

</main>
</body>
</html>
```